Biz card for my counselling/social work practice

Biz card design for my counselling practice, focus on well-being, I am a social worker who also teaches meditation and workshops but my main focus for the card is my counselling practice. My website reveals a gentle flowing quality which I would life reflected in my card. This business card will be designed to share with other practitioners who are looking for support with their clients to take their healing to another level or well-being.

Target Market(s)

professionals seeking mental health counselling/men/women/ those seeking to improve their well-being through insight based counselling to optimize their lives and process trauma or limiting patterns

Industry/Entity Type

Counsellor

Contact Information for Business Card

Info on the card: perhaps text is aligned left?
Marla Finch, MSW, RSW
Counsellor
250.555.0142
info@marlafinch.ca
www.marlafinch.ca

Please use a modern font doesn’t need to be the one chosen below. Thank you

Font styles to use
Serif

Colors
3176b5
33a6d7
33b8a4
6b449b
abd037
d2a4cc
e55fa2

Requirements
Must have
• My business card details on front
• Backside
• Accelerated Resolution Therapy
• Cognitive Behavioral Therapy
• Mindfulness Informed Therapy
Nice to have
• I would like the card to be basic, (white or creme without too much bold colour) and with perhaps a stripe or band of vertical colour in blue or green (or a merge of colour) perhaps embossed or in a negative space. (this is one idea, but do not want the card to be too feminine or interest only women as i see men too so this is only an idea, but not 100 percent on this.
• I do not have a logo. I would prefer to heart from my website not to be used in the design as i am considering modifying this and re-branding.
Should not have
• too bold colours or bright yellow/blacks. i Like tones that are greens, blues.

```html
<!DOCTYPE html>
<html lang="en">
<head>
<meta charset="utf-8">
<title>Marla Finch — Business Card</title>
<link rel="stylesheet" href="https://fonts.googleapis.com/css2?family=Source+Sans+3:wght@400&family=Source+Serif+4:opsz,wght@8..60,300;8..60,400&display=swap">
<style>
  :root {
    --sky: #36a3d6;
    --teal: #33b8a4;
    --ink: #1a1a1a;
    --grey-text: #6e6e6e;
    --paper: #ffffff;
  }
  * { margin: 0; padding: 0; box-sizing: border-box; }
  html, body {
    width: 899px;
    height: 1200px;
    overflow: hidden;
    background: var(--paper);
  }
  .sheet {
    position: relative;
    width: 899px;
    height: 1200px;
  }
  .side-label {
    position: absolute;
    left: 0;
    width: 899px;
    text-align: center;
    font-family: "Source Sans 3", sans-serif;
    font-size: 34px;
    color: var(--ink);
    letter-spacing: -0.5px;
  }
  .side-label--front { top: 42px; left: 2px; }
  .side-label--back { top: 639px; left: -12px; }

  .card {
    position: absolute;
    left: 64px;
    width: 771px;
    height: 453px;
    overflow: hidden;
  }
  .card--front { top: 130px; background: var(--paper); }
  .card--back { top: 703px; background: var(--sky); }
  .card__art {
    position: absolute;
    inset: 0;
    width: 771px;
    height: 453px;
  }

  .contact {
    position: absolute;
    left: 66px;
    top: 128px;
    font-family: "Source Serif 4", serif;
    color: var(--grey-text);
  }
  .contact__name {
    font-size: 28px;
    font-weight: 400;
    line-height: 34px;
  }
  .contact__role {
    font-size: 23px;
    font-weight: 300;
    line-height: 28px;
  }
  .contact__rule {
    width: 234px;
    height: 0;
    border-top: 1.5px solid var(--sky);
    margin: 24px 0 22px 1px;
  }
  .contact__details {
    list-style: none;
    font-size: 22px;
    font-weight: 300;
    line-height: 35.5px;
  }

  .services {
    position: absolute;
    left: 74px;
    top: 154px;
    list-style: none;
    font-family: "Source Serif 4", serif;
    font-size: 25.5px;
    font-weight: 400;
    line-height: 47.5px;
    letter-spacing: 0.4px;
    color: var(--paper);
  }
  .services li::before {
    content: "•";
    margin-right: 7px;
    font-size: 20px;
  }
</style>
</head>
<body>
<main class="sheet">
  <h2 class="side-label side-label--front">FRONT</h2>
  <section class="card card--front">
    <svg class="card__art" viewBox="0 0 771 453" aria-hidden="false">
      <path d="M475 0 Q515 220 528 453 L771 453 L771 0 Z" fill="var(--teal)"/>
      <path d="M483 0 Q524 220 537 453 L771 453 L771 0 Z" fill="var(--sky)" role="img" aria-label="Colour panel where a faint flowing script decoration belongs"/>
    </svg>
    <div class="contact">
      <h1 class="contact__name">Marla Finch, MSW, RSW</h1>
      <p class="contact__role">Counsellor</p>
      <div class="contact__rule"></div>
      <ul class="contact__details">
        <li>250.555.0142</li>
        <li>info@marlafinch.ca</li>
        <li>www.marlafinch.ca</li>
      </ul>
    </div>
  </section>

  <h2 class="side-label side-label--back">BACK</h2>
  <section class="card card--back">
    <svg class="card__art" viewBox="0 0 771 453">
      <rect x="470" y="0" width="301" height="417" fill="var(--sky)" role="img" aria-label="Area where a faint flowing script decoration belongs"/>
      <rect x="0" y="417" width="771" height="36" fill="var(--teal)"/>
    </svg>
    <ul class="services">
      <li>Accelerated Resolution Therapy</li>
      <li>Cognitive Behavioral Therapy</li>
      <li>Mindfulness Informed Therapy</li>
    </ul>
  </section>
</main>
</body>
</html>
```